Maple Lantern Business Card

Design of business cards

Target Market(s)

We are aiming as small business owners who need anything from basic business structures, website plans, business processes and quality assurance.

Industry/Entity Type

Business

Colors

Designer to choose colors to be used in the design.

Requirements
Nice to have
• I would prefer one side of the card to use the green from the logo. Prefer to have the same font as the logo.

```html
<!DOCTYPE html>
<html lang="en">
<head>
<meta charset="utf-8">
<title>Maple Lantern Consulting – Business Cards</title>
<link rel="stylesheet" href="https://fonts.googleapis.com/css2?family=Cinzel:wght@400;600&family=Lato:wght@400;700&display=swap">
<style>
  :root {
    --green: #9dc83a;
    --green-deep: #8ab82c;
    --ink: #4a4a4a;
    --ink-soft: #6b6b6b;
    --paper: #f7f7f7;
    --stage: #2b2b2b;
    --white: #ffffff;
  }
  * { box-sizing: border-box; margin: 0; padding: 0; }
  html, body { width: 1200px; height: 900px; overflow: hidden; }
  body { background: var(--stage); position: relative; font-family: "Lato", sans-serif; }

  .card {
    position: absolute;
    width: 560px;
    height: 320px;
    border-radius: 18px;
    overflow: hidden;
    box-shadow: 0 14px 30px rgba(0,0,0,.45);
  }

  /* Back side: full green */
  .card--back { left: 90px; top: 100px; background: var(--green); }
  .card--back .brand { position: absolute; left: 70px; top: 112px; display: flex; align-items: center; gap: 26px; }
  .card--back .brand-dot { width: 84px; height: 84px; border-radius: 50%; background: var(--white); }
  .card--back .brand-name { color: var(--white); }

  .brand-name {
    font-family: "Cinzel", serif;
    font-weight: 600;
    font-size: 27px;
    line-height: 1.05;
    letter-spacing: .5px;
  }

  /* Front side: white with green header band */
  .card--front { left: 550px; top: 480px; background: var(--paper); }
  .card-band {
    height: 62px;
    background: var(--green);
    text-align: right;
    padding: 12px 26px 0 0;
    color: var(--white);
  }
  .holder-name { font-family: "Cinzel", serif; font-size: 21px; letter-spacing: 1px; line-height: 1; }
  .holder-role { font-family: "Cinzel", serif; font-size: 11px; letter-spacing: 1.5px; margin-top: 3px; }

  .card--front .brand { position: absolute; left: 48px; top: 86px; display: flex; align-items: center; gap: 20px; }
  .card--front .brand-dot { width: 70px; height: 70px; border-radius: 50%; background: var(--green); }
  .card--front .brand-name { color: var(--green-deep); font-size: 24px; }

  .website {
    position: absolute; left: 48px; top: 178px;
    font-size: 13px; font-weight: 700; letter-spacing: 3.2px; color: var(--ink);
  }

  .contacts {
    position: absolute; left: 60px; top: 208px;
    display: grid; grid-template-columns: 190px 260px; row-gap: 8px;
    font-size: 14px; font-weight: 700; color: var(--ink);
  }
  .contact { display: flex; align-items: center; gap: 8px; }
  .contact svg { width: 14px; height: 14px; fill: var(--ink); flex: none; }

  .address {
    position: absolute; left: 26px; bottom: 24px;
    display: flex; align-items: center; gap: 10px;
    font-size: 14px; font-weight: 700; color: var(--ink);
  }
  .address svg { width: 16px; height: 16px; fill: var(--ink); }
</style>
</head>
<body>

  <section class="card card--back" aria-label="Card back">
    <div class="brand">
      <span class="brand-dot"></span>
      <div class="brand-name">Maple<br>Lantern<br>Consulting</div>
    </div>
  </section>

  <section class="card card--front" aria-label="Card front">
    <header class="card-band">
      <div class="holder-name">YOUR NAME</div>
      <div class="holder-role">DESIGNATION</div>
    </header>

    <div class="brand">
      <span class="brand-dot"></span>
      <div class="brand-name">Maple<br>Lantern<br>Consulting</div>
    </div>

    <div class="website">www.maplelanternco.com</div>

    <div class="contacts">
      <div class="contact">
        <svg viewBox="0 0 16 16"><path d="M2 5c0-2 3-3 6-3s6 1 6 3v1h-3V5H5v1H2zM4 7h8l2 7H2z"/></svg>
        +65 6100 2040
      </div>
      <div class="contact">
        <svg viewBox="0 0 16 16"><path d="M4 1h8v4H4zM1 6h14v6h-3v3H4v-3H1zM5 10v4h6v-4z"/></svg>
        +65 6100 2040
      </div>
      <div class="contact">
        <svg viewBox="0 0 16 16"><path d="M4 0h8a1 1 0 0 1 1 1v14a1 1 0 0 1-1 1H4a1 1 0 0 1-1-1V1a1 1 0 0 1 1-1zm1 2v10h6V2z"/></svg>
        +65 9100 3050
      </div>
      <div class="contact">
        <svg viewBox="0 0 16 16"><path d="M0 3h16v10H0zm1.5 1.2L8 9l6.5-4.8V4.2L8 8 1.5 3.8z"/></svg>
        hello@maplelanternco.com
      </div>
    </div>

    <div class="address">
      <svg viewBox="0 0 16 16"><path d="M8 1l8 7h-2v7H10v-5H6v5H2V8H0z"/></svg>
      12 Harbour Row #04-08 Lantern Works Singapore 100200
    </div>
  </section>

</body>
</html>
```